A renowned orthopaedic surgeon starting his own private clinic needs a business card design

I would need to have a design for an upcoming private clinic for orthopaedic practice.
The target market are patients that need to see a specialist for Bone and Joint Surgery.

The colors to be blue and white
Words to refer to the attached file.
Updates

Hi, Please refer to the files and a new attached file for the wordings and please attached a logo for the business card

thanks

Hi, card size is 88X 54mm

thanks

Reason: need more time to feedback

Reason: Need more time

Target Market(s)

Patients seeing for Shoulder, Elbow, wrist and hand
General Orthopaedics and Orthopaedics Trauma

Industry/Entity Type

Clinic

Colors
0355a3
eff4f7

Requirements
Must have
• follow wordings on namecard attached

```html
<!DOCTYPE html>
<html lang="en">
<head>
<meta charset="utf-8">
<title>Keystone Orthopaedics – Business Card</title>
<link rel="stylesheet" href="https://fonts.googleapis.com/css2?family=Tinos:ital,wght@0,400;1,400&family=Noto+Serif+SC:wght@400&display=swap">
<style>
  :root {
    --clinic-blue: #0355a3;
    --clinic-blue-deep: #0a4e98;
    --card-white: #eff4f7;
    --ink-white: #ffffff;
    --backdrop: #dadde0;
  }
  * { box-sizing: border-box; margin: 0; padding: 0; }
  html, body {
    width: 1200px;
    height: 960px;
    overflow: hidden;
    background: var(--backdrop);
  }
  .sheet {
    position: relative;
    width: 1200px;
    height: 960px;
  }
  .card {
    position: absolute;
    left: 270px;
    width: 660px;
    height: 405px;
    overflow: hidden;
    box-shadow: 0 2px 6px rgba(0,0,0,0.12);
  }

  /* ---------- Front ---------- */
  .card-front {
    top: 50px;
    background: linear-gradient(160deg, var(--clinic-blue-deep) 0%, var(--clinic-blue) 100%);
    color: var(--ink-white);
    font-family: "Tinos", "Times New Roman", serif;
  }
  .clinic-name {
    position: absolute;
    top: 40px;
    right: 44px;
    text-align: right;
    font-family: "Tinos", "Times New Roman", serif;
    font-weight: 400;
    font-size: 30px;
    line-height: 1.1;
    letter-spacing: 3px;
    text-transform: uppercase;
    color: var(--ink-white);
  }
  .doctor {
    position: absolute;
    left: 44px;
    top: 136px;
  }
  .doctor-name {
    font-style: italic;
    font-weight: 400;
    font-size: 40px;
    line-height: 1;
  }
  .doctor-name-zh {
    font-family: "Noto Serif SC", "Songti SC", serif;
    font-size: 19px;
    letter-spacing: 3px;
    margin-top: 6px;
  }
  .doctor-title {
    font-size: 15px;
    line-height: 1.35;
    margin-top: 10px;
  }
  .clinic-address {
    position: absolute;
    left: 44px;
    top: 268px;
    font-size: 15px;
    line-height: 1.35;
    font-style: normal;
  }
  .contact {
    position: absolute;
    left: 370px;
    top: 322px;
    font-size: 16px;
    line-height: 1.4;
  }

  /* ---------- Back ---------- */
  .card-back {
    top: 505px;
    background: var(--card-white);
    color: var(--clinic-blue);
  }
  .tag {
    display: inline-block;
    background: var(--clinic-blue);
    color: var(--ink-white);
    border-radius: 5px;
    padding: 3px 8px;
  }
  .interest-en {
    position: absolute;
    left: 48px;
    top: 56px;
    font-family: "Tinos", "Times New Roman", serif;
    font-size: 17px;
    line-height: 1.4;
  }
  .interest-en .tag {
    font-size: 15px;
    letter-spacing: 0.5px;
    margin-bottom: 10px;
  }
  .interest-zh {
    position: absolute;
    left: 360px;
    top: 200px;
    font-family: "Noto Serif SC", "Songti SC", serif;
    font-size: 22px;
    line-height: 1.8;
    letter-spacing: 6px;
  }
  .interest-zh .tag {
    font-size: 17px;
    letter-spacing: 2px;
    padding: 2px 8px;
    margin-bottom: 4px;
  }
</style>
</head>
<body>
<main class="sheet">

  <section class="card card-front" aria-label="Business card front">
    <div class="clinic-name">Keystone<br>Orthopaedics</div>

    <div class="doctor">
      <h1 class="doctor-name">Dr Tan Wei-Ming</h1>
      <p class="doctor-name-zh" lang="zh">陈伟明医生</p>
      <p class="doctor-title">Consultant Orthopaedic Surgeon<br>MBBS (Singapore), MMed (Ortho), FRCSEd (Ortho)</p>
    </div>

    <address class="clinic-address">
      Harbourview Medical Centre<br>
      #05-12, 18 Kellock Lane, Singapore 248733
    </address>

    <p class="contact">
      Tel: +65 8000 1234<br>
      Email: drtanweiming@example.com
    </p>
  </section>

  <section class="card card-back" aria-label="Business card back">
    <div class="interest-en">
      <span class="tag">SPECIAL INTEREST IN:</span>
      <p>Shoulder, Elbow, Wrist and Hand</p>
      <p>General Orthopaedics and</p>
      <p>Orthopaedic Trauma</p>
    </div>

    <div class="interest-zh" lang="zh">
      <span class="tag">专业:</span>
      <p>肩，肘，腕，手</p>
      <p>骨外科，骨伤科</p>
    </div>
  </section>

</main>
</body>
</html>
```